Rollin’ Kites Copper Tide beer can design

We are not looking for a new logo, we want to use our current logo!! Current Logo is Attached. We want to incorporate our current logo into a full can design for our new non-alcoholic, THC infused Beer design. We cannot use animals or cartoons. We also can not say beer. We would like to use our main label found at www.rollinkites-example.com
Several ideas include having small images of beer cans and beer mugs all over the can as a background. Another idea is to make it freedom and liberty themed. We want to make sure people understand it is a beer, even though we can say beer on the can.

Target Market(s)

30-50 year olds

Industry/Entity Type

THC beverage

Logo Text

Rollin’ Kites Copper Tide

Colors
59FF00
82FF00
B8FF75
E3FFCB
F4FFEA

Requirements
Must have
• Full 12 oz beer can design
Should not have
• No word beer, do not need a new logo, need a can design

```html
<!DOCTYPE html>
<html lang="en">
<head>
<meta charset="utf-8">
<title>Rollin’ Kites Copper Tide – Copper Wave Lift can label</title>
<link href="https://fonts.googleapis.com/css2?family=Oswald:wght@500;700&family=Allura&display=swap" rel="stylesheet">
<style>
  :root{
    --stage:#98ab5e;
    --label-light:#e3f2cb;
    --label-mid:#b8e07a;
    --label-green:#5fae2e;
    --band-dark:#0f4a26;
    --band-mid:#2f7f2c;
    --ink:#141414;
    --script:#e6ece0;
    --badge-ring:#1f4d2a;
  }
  html,body{margin:0;padding:0;width:1200px;height:1082px;overflow:hidden;background:var(--stage);}
  .canvas{position:relative;width:1200px;height:1082px;}
  .can-label{
    position:absolute;left:330px;top:80px;width:540px;height:920px;
    border-radius:18px;overflow:hidden;
    background:linear-gradient(180deg,var(--label-green) 0%,#7cc63e 55%,var(--band-mid) 100%);
    box-shadow:0 20px 40px rgba(40,60,20,.25);
  }
  .pattern-field{
    position:absolute;left:0;top:0;width:540px;height:610px;
    background:
      radial-gradient(ellipse at 30% 30%,rgba(255,255,255,.55),rgba(255,255,255,0) 60%),
      linear-gradient(160deg,#9fd65a 0%,var(--label-light) 45%,var(--label-mid) 100%);
    border-bottom-left-radius:50% 40px;border-bottom-right-radius:50% 40px;
  }
  .brand-badge{
    position:absolute;left:0;right:0;top:200px;
    display:flex;align-items:center;justify-content:center;gap:20px;
  }
  .brand-badge .mark-dot{
    width:54px;height:54px;border-radius:50%;background:var(--badge-ring);flex:none;
  }
  .brand-badge .brand-name{
    font-family:'Oswald',sans-serif;font-weight:700;font-size:56px;line-height:1.1;
    color:var(--ink);text-transform:uppercase;letter-spacing:1px;white-space:nowrap;
  }
  .tagline{
    position:absolute;left:0;right:0;top:480px;text-align:center;
    font-family:'Oswald',sans-serif;font-weight:700;font-size:46px;color:var(--ink);
    text-transform:uppercase;letter-spacing:.5px;
  }
  .dose{
    position:absolute;left:0;right:0;top:630px;text-align:center;
    font-family:'Oswald',sans-serif;font-weight:700;font-size:30px;color:var(--ink);
  }
  .zigzag-band{position:absolute;left:0;top:690px;width:540px;height:170px;}
  .flavor{
    position:absolute;left:0;right:0;top:732px;text-align:center;
    font-family:'Allura',cursive;font-size:68px;line-height:1;color:var(--script);
  }
  .volume{
    position:absolute;left:0;right:0;top:866px;text-align:center;
    font-family:'Oswald',sans-serif;font-weight:700;font-size:28px;line-height:1;color:var(--ink);
  }
</style>
</head>
<body>
<main class="canvas">
  <section class="can-label">
    <div class="pattern-field" role="img" aria-label="Faint repeating pattern of small cans, mugs and leaves over soft light-green swirls"></div>

    <div class="brand-badge">
      <span class="mark-dot"></span>
      <span class="brand-name">Rollin’ Kites<br>Copper Tide</span>
    </div>

    <div class="tagline">“Sip the calm tide”</div>

    <div class="dose">10 MG THC</div>

    <svg class="zigzag-band" viewBox="0 0 540 170" aria-hidden="true">
      <defs>
        <pattern id="teeth-top" width="30" height="24" patternUnits="userSpaceOnUse">
          <path d="M0 24 L15 0 L30 24Z" fill="var(--band-dark)"/>
        </pattern>
        <pattern id="teeth-bottom" x="0" y="146" width="30" height="24" patternUnits="userSpaceOnUse">
          <path d="M0 0 L15 24 L30 0Z" fill="var(--band-dark)"/>
        </pattern>
      </defs>
      <rect x="0" y="0" width="540" height="24" fill="url(#teeth-top)"/>
      <rect x="0" y="24" width="540" height="122" fill="var(--band-dark)"/>
      <rect x="0" y="146" width="540" height="24" fill="url(#teeth-bottom)"/>
    </svg>

    <div class="flavor">Copper Wave Lift</div>

    <div class="volume">12 OZ</div>
  </section>
</main>
</body>
</html>
```